Bottle label design for 4 litre jug

Need to create a label for my chemical products please attached label. Must have the side labels, colors must be complimented with logo attached. Come up with a clean yet high end product look to it. the brand name is Vantor Glass cleaner, Tandel shine solutions is the logo,
Redisgn with new updated look, there are a total of 8 labels to be made for oterh products.

Industry/Entity Type

Cleaning industry

Font styles to use
Serif
Other font styles liked:
• Lora Bold, EB garamond, or use any font you choose, clean and bold

Colors
0054AA
0677BA
7BADD7
CADEEF
E8F1F8
0094D4
00A9DD
6FCCEA
C7EBF8
E9F6FB
00AB8E
00BBA5
67D7C9
C6EFE9
E9F9F6

```html
<!DOCTYPE html>
<html lang="en">
<head>
<meta charset="utf-8">
<title>Vantor Glass Cleaner – 4L Label</title>
<link rel="stylesheet" href="https://fonts.googleapis.com/css2?family=Montserrat:wght@700;800&family=Barlow:wght@500;600;700&family=Barlow+Condensed:wght@500&display=swap">
<style>
  :root {
    --navy: #0054AA;
    --blue: #0677BA;
    --sky: #0094D4;
    --cyan: #00A9DD;
    --light-blue: #7BADD7;
    --pale-blue: #C7EBF8;
    --mist: #E9F6FB;
    --teal: #00AB8E;
    --teal-2: #00BBA5;
    --teal-light: #67D7C9;
    --ink: #1a1a1a;
    --hazard: #d8262c;
    --page: #eef1f4;
    --label: #ffffff;
  }
  * { box-sizing: border-box; margin: 0; padding: 0; }
  html, body { width: 1200px; height: 1200px; overflow: hidden; }
  body { background: var(--page); position: relative; font-family: "Barlow", sans-serif; color: var(--ink); }

  .label {
    position: absolute; left: 0; top: 294px; width: 1200px; height: 612px;
    background: var(--label); overflow: hidden;
  }

  /* side panels */
  .side { position: absolute; }
  .side-left { left: 35px; top: 0; width: 207px; }
  .side-right { left: 939px; top: 0; width: 243px; }
  .side-title {
    position: absolute; top: 76px; left: 0; width: 207px; text-align: center;
    font-weight: 700; font-size: 16.5px; color: var(--blue); letter-spacing: .3px;
  }
  .body-copy {
    position: absolute; left: 0; font-weight: 500; font-size: 12px; line-height: 15.8px;
    text-align: justify; hyphens: auto;
  }
  .side-left .body-copy { width: 207px; }
  .side-right .body-copy { width: 243px; }
  .hazard { position: absolute; left: 111px; top: 241px; width: 55px; height: 55px; }
  .maker {
    position: absolute; top: 537px; left: 0; width: 207px; text-align: center;
    font-weight: 700; font-size: 12.5px; line-height: 14.5px;
  }

  /* front panel */
  .brand {
    position: absolute; left: 510px; top: 50px; display: flex; align-items: center; gap: 8px;
  }
  .brand-dot { width: 30px; height: 30px; border-radius: 50%; background: var(--teal); }
  .brand-name {
    font-family: "Barlow", sans-serif; font-weight: 600; font-size: 13.5px; line-height: 13.5px;
    color: var(--navy); text-transform: uppercase;
  }
  .product-name {
    position: absolute; left: 300px; width: 590px; top: 128px; text-align: center;
    font-family: "Montserrat", sans-serif; font-weight: 800; font-size: 70px; line-height: 68px;
    letter-spacing: -1px;
    background: linear-gradient(90deg, var(--navy) 0%, var(--blue) 55%, var(--cyan) 100%);
    -webkit-background-clip: text; background-clip: text; color: transparent;
  }
  .claim-pill {
    position: absolute; left: 422px; top: 276px; width: 345px; height: 47px; border-radius: 24px;
    background: linear-gradient(90deg, var(--blue), var(--teal-2));
    color: #fff; text-align: center; font-weight: 500; font-size: 13.5px; line-height: 16px;
    letter-spacing: .3px; padding-top: 7px;
  }
  .claim-fr {
    position: absolute; left: 380px; width: 430px; top: 336px; text-align: center;
    font-family: "Barlow Condensed", sans-serif; font-weight: 500; font-size: 16px; line-height: 17.5px;
    color: var(--blue);
  }
  .wave {
    position: absolute; left: 378px; top: 352px; width: 536px; height: 260px;
  }
  .feature-badges { position: absolute; left: 471px; top: 394px; display: flex; gap: 19px; }
  .feature-badge {
    width: 70px; height: 70px; border-radius: 50%;
    background: radial-gradient(circle, var(--teal-2) 0 40%, var(--sky) 41% 100%);
    border: 3px solid #fff; box-shadow: 0 0 0 1px var(--light-blue);
  }
  .eco-marks { position: absolute; left: 821px; top: 245px; display: flex; flex-direction: column; gap: 13px; }
  .eco-mark { width: 77px; border: 2px dashed var(--teal); border-radius: 4px; }
  .eco-mark.short { height: 31px; }
  .eco-mark.tall { height: 60px; }
  .qms { position: absolute; left: 348px; top: 500px; display: flex; align-items: center; gap: 6px; }
  .qms svg { width: 32px; height: 32px; }
  .qms-text { font-weight: 700; font-size: 13.5px; line-height: 17px; color: var(--blue); letter-spacing: .3px; }
  .volume {
    position: absolute; left: 348px; top: 552px; width: 63px; height: 30px; border-radius: 12px;
    background: linear-gradient(90deg, var(--navy), var(--blue));
    color: #fff; font-family: "Montserrat", sans-serif; font-weight: 700; font-size: 22px;
    line-height: 30px; text-align: center;
  }
</style>
</head>
<body>
<main class="label">

  <section class="side side-left">
    <h2 class="side-title">VANTOR GLASS CLEANER</h2>
    <p class="body-copy" style="top:112px">Lorem ipsum dolor sit amet, consectetuer adipiscing elit, sed diam nonummy nibh euismod tincidunt ut laoreet dolore magna aliquam erat volutpat. Ut wisi enim ad minim veniam, quis nostrud exerci tation ullamcorper</p>
    <svg class="hazard" viewBox="0 0 60 60" aria-label="Warning">
      <rect x="12" y="12" width="36" height="36" transform="rotate(45 30 30)" fill="#fff" stroke="var(--hazard)" stroke-width="3"/>
      <rect x="27.5" y="17" width="5" height="18" rx="2" fill="#111"/>
      <circle cx="30" cy="41" r="3" fill="#111"/>
    </svg>
    <p class="body-copy" style="top:307px">Lorem ipsum dolor sit amet, consectetuer adipiscing elit, sed diam nonummy nibh euismod tincidunt ut laoreet dolore magna aliquam erat volutpat. Ut wisi enim ad minim veniam, quis nostrud exerci tation ullamcorper suscipit lobortis nisl ut aliquip ex ea commodo consequat. Duis</p>
    <p class="maker">TANDEL SHINE SOLUTIONS<br>Harrowgate, Ontario L0X 2Y4</p>
  </section>

  <div class="wave" role="img" aria-label="Soft flowing blue line wave decoration"
       style="background: radial-gradient(ellipse 90% 120% at 100% 100%, var(--light-blue) 0%, var(--pale-blue) 45%, rgba(233,246,251,0) 75%), radial-gradient(ellipse 60% 80% at 95% 5%, rgba(0,148,212,.55), rgba(255,255,255,0) 70%);"></div>

  <section class="front">
    <div class="brand">
      <span class="brand-dot"></span>
      <span class="brand-name">Tandel<br>Shine<br>Solutions</span>
    </div>
    <h1 class="product-name">VANTOR GLASS<br>CLEANER</h1>
    <p class="claim-pill">Dries fast without leaving a film or streaking.<br>Polishes as it dissolves dirt &amp; dingy film.</p>
    <p class="claim-fr">Sans laisser de pellicules ni de trainées.<br>Dissout saleté et pellicule teme et fait briller.</p>
    <div class="feature-badges">
      <span class="feature-badge"></span>
      <span class="feature-badge"></span>
      <span class="feature-badge"></span>
    </div>
    <div class="eco-marks">
      <span class="eco-mark short"></span>
      <span class="eco-mark tall"></span>
    </div>
    <div class="qms">
      <svg viewBox="0 0 32 32" aria-hidden="true">
        <circle cx="15" cy="17" r="12" fill="none" stroke="var(--navy)" stroke-width="2.5"/>
        <path d="M8 16 L14 23 L29 5" fill="none" stroke="var(--sky)" stroke-width="4" stroke-linecap="round" stroke-linejoin="round"/>
      </svg>
      <p class="qms-text">COMPLIANT QMS<br>Mfg. Process</p>
    </div>
    <div class="volume">4L</div>
  </section>

  <section class="side side-right">
    <p class="body-copy" style="top:82px">Lorem ipsum dolor sit amet, consectetuer adipiscing elit, sed diam nonummy nibh euismod tincidunt ut laoreet dolore magna aliquam erat volutpat. Ut wisi enim ad minim veniam,</p>
    <p class="body-copy" style="top:209px">Lorem ipsum dolor sit amet, consectetuer adipiscing elit, sed diam nonummy nibh euismod tincidunt ut laoreet dolore magna aliquam erat volutpat. Ut wisi enim ad minim veniam,</p>
    <p class="body-copy" style="top:323px">Lorem ipsum dolor sit amet, consectetuer adipiscing elit, sed diam nonummy nibh euismod tincidunt ut laoreet dolore magna aliquam erat volutpat. Ut wisi enim ad minim veniam,</p>
    <p class="body-copy" style="top:442px">Lorem ipsum dolor sit amet, consectetuer adipiscing elit, sed diam nonummy nibh euismod tincidunt ut laoreet dolore magna aliquam erat volutpat. Ut wisi enim ad minim veniam,</p>
  </section>

</main>
</body>
</html>
```